Brightfold Reach - B2B Demand Generation Website Project

We need a fully functional website for www.brightfoldreach-example.com. We are a B2B Demand Generation company, based in London, working with companies such as QTR, DWN, Vortan, Brelloway, Pelta generating them sales leads for their sales teams. We run this through digital marketing newsletter promotions and have a network of websites. Content syndication, data, demand generation, online marketing. Our logo has just been redone (attached) and we have a holding page already which i would like to use the style / colours. Our logo is bright and vibrant but i dont want the site to be a rainbow. We are expensive, classy, professorial, B2B, intelligent.

Home
About Us
Our Services
Prospero & QA Technology
Intent Data
Testimonials
Contact Us

Target Market(s)

B2B Marketers (QTR, Quorvane, Pelta, DWN, Vista Hub, Harrowby, Tremont Axis, Technology Companies, Data Companies, Marketing Teams, Cloudwick.

Industry/Entity Type

Marketing

Coding

Coded - Design and coding required

Number of Pages Required

5+ page

Font styles to use
Sans Serif

Requirements
Must have
• Home
About Us
Our Services
Prospero & QA Technology
Intent Data
Testimonials
Contact Us

Simple Pages.

Look classy, intelligent, data experts. I like the video homepages were the image moves at the top. Very soft animation.
Nice to have
• Websites i like:

https://www.dwn-example.com/
https://www.pulsegate-example.com/
https://www.lmsitecraft-example.co.uk/

Brightfold Reach - The Demand Generation Company
Should not have
• Pixelvault crap images

```html
<!DOCTYPE html>
<html lang="en">
<head>
<meta charset="utf-8">
<title>Brightfold Reach - The Demand Generation Company</title>
<link href="https://fonts.googleapis.com/css2?family=Montserrat:wght@400;500;600;700;800&display=swap" rel="stylesheet">
<style>
:root{
  --red:#c0201f;
  --red-dark:#a31818;
  --blue:#1d5ca6;
  --ink:#111111;
  --text:#333333;
  --muted:#666666;
  --night:#0c131c;
  --footer:#1c1c1e;
  --grey-band:#e4e5e7;
  --white:#ffffff;
}
*{box-sizing:border-box;margin:0;padding:0}
html,body{width:1200px;height:3678px;overflow:hidden}
body{font-family:"Montserrat",Arial,sans-serif;color:var(--text);background:var(--white);position:relative}
.abs{position:absolute}
.btn{position:absolute;background:var(--blue);color:var(--white);font-size:18px;font-weight:500;display:flex;align-items:center;justify-content:center;height:41px}

/* hero */
.hero{position:absolute;left:0;top:0;width:1200px;height:571px;background:linear-gradient(100deg,#070b11 0%,#0d1620 45%,#1d2f45 75%,#2a4664 100%)}
.brand{position:absolute;display:flex;align-items:center;gap:10px}
.brand-dot{width:34px;height:34px;border-radius:50%;background:var(--red)}
.brand-name{font-size:27px;font-weight:600;color:var(--red);letter-spacing:-.3px}
.brand-tag{position:absolute;font-size:9px;color:var(--blue);font-weight:500}
.nav{position:absolute;left:349px;top:57px;display:flex;gap:22px;font-size:14.5px;color:var(--white)}
.nav .on{color:var(--red)}
.hero h1{position:absolute;left:98px;top:246px;font-size:51px;font-weight:800;color:var(--white);letter-spacing:-.5px}
.hero h1 .r{color:var(--red)}
.hero h1 .b{color:var(--blue)}
.hero p{position:absolute;left:99px;top:312px;width:560px;font-size:18.5px;line-height:24px;color:var(--white)}

/* stats */
.stats{position:absolute;left:0;top:571px;width:1200px;height:175px;display:flex}
.stat{flex:1;background:var(--red);color:var(--white);text-align:center;padding-top:34px}
.stat.mid{background:var(--red-dark);flex:0 0 405px}
.stat .lbl{font-size:18px;line-height:29px}
.stat .num{font-size:42px;font-weight:500;margin-top:4px}

/* about */
.about-frame{position:absolute;left:137px;top:843px;width:407px;height:257px;border:3px solid var(--red)}
.photo{position:absolute}
.about h2,.section-title{font-weight:800;color:var(--ink);letter-spacing:-.3px}
.about h2{position:absolute;left:613px;top:802px;font-size:43px}
.about .lead{position:absolute;left:613px;top:861px;width:500px;font-size:18px;line-height:24px;color:var(--ink)}
.about .body{position:absolute;left:613px;top:925px;width:510px;font-size:13.5px;line-height:24px;color:var(--text)}

/* services */
.services{position:absolute;left:0;top:1210px;width:1200px;height:547px;background:linear-gradient(180deg,#dcdddf,#eeeeef 50%,#dcdde0)}
.section-title{position:absolute;width:1200px;text-align:center;font-size:43px}
.card{position:absolute;top:144px;width:316px;height:336px;background:var(--white);border:1px solid #d8d8d8;text-align:center}
.card svg{margin-top:26px}
.card h3{font-size:16px;font-weight:700;color:var(--ink);line-height:23px;margin-top:10px}
.card p{font-size:13.5px;line-height:20px;color:var(--text);margin:18px 14px 0}
.card .more{display:block;margin-top:16px;color:var(--blue);font-size:17px;font-weight:500}

/* qa */
.qa h2{position:absolute;left:98px;top:1822px;font-size:43px}
.qa p{position:absolute;left:98px;top:1888px;width:510px;font-size:14.5px;line-height:24px}
.product{position:absolute;left:710px;top:1900px;display:flex;align-items:center;gap:18px}
.product-sq{width:46px;height:46px;background:var(--red)}
.product-name{font-size:62px;font-weight:500;color:#2d3540;letter-spacing:6px}

/* intent */
.intent{position:absolute;left:0;top:2214px;width:1200px;height:389px;background:linear-gradient(180deg,#e1e1e1,#ececec 50%,#e1e1e1)}
.intent p{position:absolute;left:120px;top:126px;width:960px;text-align:center;font-size:14.5px;line-height:24px}

/* testimonials */
.tcard{position:absolute;top:2757px;height:296px;background:var(--white);border:1px solid #dcdcdc}
.tcard.side{opacity:.55}
.avatar{position:absolute;left:22px;top:22px;width:96px;height:102px;background:linear-gradient(160deg,#4a6f76,#2f4a50)}
.tname{position:absolute;left:135px;top:54px;font-size:17px;font-weight:700;color:var(--ink)}
.tjob{position:absolute;left:135px;top:80px;font-size:13.5px;font-weight:600;color:var(--ink)}
.tquote{position:absolute;left:22px;top:145px;width:470px;font-size:14.5px;line-height:20.5px;color:var(--text)}
.qmark{position:absolute;top:0;width:56px;height:48px;background:var(--red);color:var(--white);font-size:64px;font-weight:800;line-height:70px;text-align:center}
.dots{position:absolute;left:584px;top:3083px;display:flex;gap:3px}
.dots span{width:8px;height:7px;background:#9ab6d8}
.dots .on{background:var(--blue)}

/* partners */
.partners{position:absolute;left:0;top:3161px;width:1200px;height:183px;background:var(--red);display:flex;align-items:center;padding-left:98px;gap:0}
.partner{color:var(--white);font-weight:700;font-size:44px;letter-spacing:1px}

/* footer */
.footer{position:absolute;left:0;top:3344px;width:1200px;height:334px;background:linear-gradient(180deg,#232325,#141416)}
.footer h4{position:absolute;top:77px;font-size:18px;font-weight:500;color:var(--white)}
.finfo{position:absolute;left:361px;top:114px;width:240px;font-size:13px;line-height:25px;color:var(--white)}
.finfo .k{color:var(--red)}
.flinks{position:absolute;left:653px;top:119px;font-size:14.5px;line-height:21px;color:var(--white)}
.fbar{position:absolute;left:0;top:280px;width:1200px;border-top:1px solid #3a3a3c}
.copy{position:absolute;left:98px;top:302px;font-size:12.5px;color:var(--white)}
.social{position:absolute;left:981px;top:302px;display:flex;gap:14px}
.social span{width:16px;height:16px;border-radius:50%;background:var(--red)}
</style>
</head>
<body>

<header class="hero" role="img" aria-label="Dark blue photo of business silhouettes over a glowing data network">
  <div class="brand" style="left:98px;top:78px">
    <span class="brand-dot"></span><span class="brand-name">Brightfold Reach</span>
  </div>
  <div class="brand-tag" style="left:142px;top:122px">The Demand Generation Company</div>
  <nav class="nav">
    <span class="on">Home</span><span>About Us</span><span>Our Services</span><span>Prospero &amp; QA Technology</span><span>Intent Data</span><span>Testimonials</span><span>Contact Us</span>
  </nav>
  <h1><span class="r">Brightfold</span> <span class="b">Reach</span> Offers</h1>
  <p>Multi-channel demand generation services to publishers and technology vendors through our network of lead generation websites and native speaking telemarketing agents.</p>
  <div class="btn" style="left:98px;top:411px;width:139px">Know More</div>
</header>

<section class="stats">
  <div class="stat"><div class="lbl">Downloads Per Month<br>Ticker to</div><div class="num">70,000+</div></div>
  <div class="stat mid"><div class="lbl">Leads Delivered Per Month<br>Ticker</div><div class="num">25,000+</div></div>
  <div class="stat" style="padding-top:38px"><div class="lbl">Countries We Can Reach<br>Ticker to</div><div class="num">50+</div></div>
</section>

<section class="about">
  <div class="about-frame"></div>
  <div class="photo" role="img" aria-label="Hands reviewing printed charts on a desk" style="left:97px;top:811px;width:312px;height:250px;background:linear-gradient(135deg,#6b7f96,#c9b8a6 60%,#e6e2dc)"></div>
  <div class="photo" role="img" aria-label="Team discussing notes on a whiteboard in a bright office" style="left:276px;top:887px;width:311px;height:252px;background:linear-gradient(160deg,#e9ecef,#b9bfc6 55%,#5d6b7c)"></div>
  <h2>ABOUT US</h2>
  <p class="lead">Brightfold Reach can deliver high quality sales leads from any country in the world.</p>
  <p class="body">Brightfold Reach can include leads via email or telemarketing, account-based targeting (ABM) or identifying need and pain points through BANT / SQL campaigns.<br>Brightfold Reach offer expert demand generation support, from providing detailed leads of qualified decision-makers, to a comprehensive lead generation and SQL service.</p>
  <div class="btn" style="left:612px;top:1087px;width:137px">Know More</div>
</section>

<section class="services">
  <h2 class="section-title" style="top:62px">OUR SERVICES</h2>
  <div class="card" style="left:99px">
    <svg width="80" height="80" viewBox="0 0 80 80" fill="none" stroke-width="3"><circle cx="40" cy="34" r="28" stroke="#2b2f6a"/><circle cx="40" cy="34" r="18" stroke="#c0201f"/><circle cx="40" cy="34" r="7" stroke="#2b2f6a"/><path d="M40 34v40" stroke="#c0201f"/></svg>
    <h3>MARKETING QUALIFIED<br>LEADS (MQL)</h3>
    <p>A Marketing Qualified Lead (MQL) is a prospect that has expressed an interest in what your brand has to offer.</p>
    <span class="more">Read More</span>
  </div>
  <div class="card" style="left:441px">
    <svg width="80" height="80" viewBox="0 0 80 80" fill="none" stroke-width="3"><circle cx="40" cy="36" r="15" stroke="#2b2f6a"/><text x="40" y="43" font-size="20" text-anchor="middle" fill="#2b2f6a" stroke="none" font-family="Montserrat,sans-serif">$</text><path d="M8 64h18l14 6 30-14" stroke="#c0201f"/><path d="M40 4v10M28 8l3 8M52 8l-3 8" stroke="#2b2f6a"/></svg>
    <h3>ACCOUNT BASED MARKETING<br>LEADS (ABM</h3>
    <p>ABM is a strategy that directs marketing resources to engaging a specific set of target accounts.</p>
    <span class="more">Read More</span>
  </div>
  <div class="card" style="left:786px">
    <svg width="80" height="80" viewBox="0 0 80 80" fill="none" stroke-width="3"><circle cx="30" cy="34" r="24" stroke="#2b2f6a"/><circle cx="44" cy="40" r="16" stroke="#c0201f"/><path d="M56 52l16 16" stroke="#c0201f" stroke-width="5"/></svg>
    <h3>SALES QUALIFIED<br>LEAD / BANT</h3>
    <p>An SQL lead or a BANT lead is a type of lead that expressed a specific interest in a product and service</p>
    <span class="more">Read More</span>
  </div>
</section>

<section class="qa">
  <h2 class="section-title" style="left:98px;top:1822px;width:auto;text-align:left">QA TECHNOLOGY</h2>
  <p>Prospero is a proprietary lead verification platform from Brightfold Reach that aims to sift out invalid leads with questionable or erroneous data. The platform is designed to equip sales teams with accurate, high-quality records in order to improve lead generation, accelerate pipeline and increase revenue.<br>Prospero is positioned to quickly identify, validate, and improve lead quality at the point-of-entry by filtering out all leads that do not match required filters, such as job title, company size, etc.</p>
  <div class="btn" style="left:98px;top:2103px;width:137px">Know More</div>
  <div class="product"><span class="product-sq"></span><span class="product-name">PROSPERO</span></div>
</section>

<section class="intent" role="img" aria-label="Light grey background of faint binary data columns">
  <h2 class="section-title" style="top:72px">INTENT DATA</h2>
  <p>Our relationships with the world's most important technology &amp; business decisions-makers generate a perpetual stream of global data. With access to 35 million individuals and a global behavioural data stream that is authenticated, timely and contextually relevant, we have one of the industry's most powerful signals of buyer intent and can fuel your demand-generation marketing strategies globally. We support our Intent targeting capabilities by partnering with a number of third party intent providers, meaning we are able to target the global data universe to deliver the best and most engaging leads to our partners.</p>
  <div class="btn" style="left:531px;top:279px;width:137px">Know More</div>
</section>

<section class="testimonials">
  <h2 class="section-title" style="top:2664px">OUR TESTIMONIALS</h2>
  <div class="tcard side" style="left:-197px;width:514px">
    <div class="avatar" role="img" aria-label="Client portrait"></div>
    <div class="tname">Lorem Ipsum</div><div class="tjob">Job Title</div>
    <p class="tquote">“Lorem ipsum dolor sit amet, consectetur adipiscing elit, sed do eiusmod tempor incididunt ut labore et dolore magna aliqua. Ut enim ad minim veniam, quis nostrud exercitation ullamco laboris nisi ut aliquip ex ea commodo consequat. Duis aute irure dolor in reprehenderit in voluptate velit esse cillum dolore eu fugiat nulla pariatur. Excepteur sint occaecat cupidatat non proident, sunt in culpa qui officia deserunt mollit anim id est laborum.”</p>
    <div class="qmark" style="left:456px">”</div>
  </div>
  <div class="tcard" style="left:343px;width:514px">
    <div class="avatar" role="img" aria-label="Client portrait"></div>
    <div class="tname">Lorem Ipsum</div><div class="tjob">Job Title</div>
    <p class="tquote">“Lorem ipsum dolor sit amet, consectetur adipiscing elit, sed do eiusmod tempor incididunt ut labore et dolore magna aliqua. Ut enim ad minim veniam, quis nostrud exercitation ullamco laboris nisi ut aliquip ex ea commodo consequat. Duis aute irure dolor in reprehenderit in voluptate velit esse cillum dolore eu fugiat nulla pariatur. Excepteur sint occaecat cupidatat non proident, sunt in culpa qui officia deserunt mollit anim id est laborum.”</p>
    <div class="qmark" style="left:456px">”</div>
  </div>
  <div class="tcard side" style="left:886px;width:514px">
    <div class="avatar" role="img" aria-label="Client portrait" style="background:linear-gradient(160deg,#8fb8a0,#4d7f64)"></div>
    <div class="tname">Lorem Ipsum</div><div class="tjob">Job Title</div>
    <p class="tquote">“Lorem ipsum dolor sit amet, consectetur adipiscing elit, sed do eiusmod tempor incididunt ut labore et dolore magna aliqua. Ut enim ad minim veniam, quis nostrud exercitation ullamco laboris nisi ut aliquip ex ea commodo consequat. Duis aute irure dolor in reprehenderit in voluptate velit esse cillum dolore eu fugiat nulla pariatur. Excepteur sint occaecat cupidatat non proident, sunt in culpa qui officia deserunt mollit anim id est laborum.”</p>
  </div>
  <div class="dots"><span></span><span class="on"></span><span></span></div>
</section>

<section class="partners">
  <span class="partner" style="width:182px">QTR</span>
  <span class="partner" style="width:188px">Pelta</span>
  <span class="partner" style="width:222px">DWN</span>
  <span class="partner" style="width:210px">Norveld</span>
  <span class="partner">Tallyrun</span>
</section>

<footer class="footer">
  <div class="brand" style="left:97px;top:112px">
    <span class="brand-dot" style="width:30px;height:30px"></span><span class="brand-name" style="font-size:25px">Brightfold Reach</span>
  </div>
  <div class="brand-tag" style="left:137px;top:152px">The Demand Generation Company</div>
  <h4 style="left:361px">Contact Info</h4>
  <div class="finfo"><span class="k">Address:</span> Lorem ipsum dolor sit amet, consectetur adipiscing elit<br><span class="k">Phone:</span> 000-000-000<br><span class="k">Email:</span> hello@brightfoldreach-example.com</div>
  <h4 style="left:653px">Useful Links</h4>
  <div class="flinks">Home<br>About Us<br>Our Services<br>Prospero &amp; QA Technology<br>Intent Data<br>Testimonials<br>Contact Us</div>
  <h4 style="left:869px">Location</h4>
  <div role="img" aria-label="Street map showing the office location" style="position:absolute;left:869px;top:110px;width:232px;height:136px;background:linear-gradient(135deg,#e8e4d8,#d8e2cf 60%,#cfd9e3)"></div>
  <div class="fbar"></div>
  <div class="copy">©2020 By Brightfold Reach. All rights reserved</div>
  <div class="social"><span></span><span></span><span></span><span></span></div>
</footer>

</body>
</html>
```